Email Signature

We are looking for creative email signature for our company. Please find attached the logo of our company for your reference. now we understand there isn't much can be done with email signature but we are looking for out of the box designs. Nothing specific in mind

Please insert fake numbers, website and/or address, etc just to showcase the designs. once the design is chosen we will provide the actual details.
Updates

Dear All,

We wouldlike to extend our apology for not being able to provide feedbacks to everysingle design. We were extremely busy and we have multiple contests opensimultaneously which makes the process harder. However, thank you all for theefforts you have put into this contest. We have received anoverwhelming quality responses & it has been a very difficult task tochoose just one, we easily Loved at least several designs...

Thanksagain for participating, we wish you all success in your design ventures.

Kindregards,

HLW Team

Industry/Entity Type

It Company

```html
<!DOCTYPE html>
<html lang="en">
<head>
<meta charset="utf-8">
<title>Harbor Lantern Email Signature</title>
<link rel="stylesheet" href="https://fonts.googleapis.com/css2?family=Arimo:wght@400;700&display=swap">
<style>
  :root {
    --blue: #3d8ff5;
    --blue-band: #3a8ef6;
    --green: #7ee62a;
    --ink: #111111;
    --paper: #ffffff;
  }
  * { margin: 0; padding: 0; box-sizing: border-box; }
  html, body {
    width: 1200px;
    height: 1000px;
    overflow: hidden;
    background: var(--paper);
    font-family: "Arimo", Arial, sans-serif;
  }
  .signature {
    position: relative;
    width: 1200px;
    height: 1000px;
  }
  .brand-name {
    position: absolute;
    left: 310px;
    top: 440px;
    font-size: 40px;
    font-weight: 700;
    color: var(--blue);
    letter-spacing: -0.5px;
    white-space: nowrap;
  }
  .contact-list {
    position: absolute;
    left: 311px;
    top: 507px;
    list-style: none;
    font-size: 13px;
    line-height: 15.5px;
    color: var(--ink);
  }
  .contact-list .label { color: var(--green); margin-right: 4px; }
  .web-links {
    position: absolute;
    left: 311px;
    top: 568px;
    font-size: 13px;
    line-height: 15.5px;
    color: var(--blue);
  }
  .social-icons {
    position: absolute;
    left: 840px;
    top: 519px;
    display: flex;
    align-items: center;
    gap: 6px;
  }
  .address-band {
    position: absolute;
    left: 293px;
    top: 605px;
    width: 635px;
    height: 21px;
    background: linear-gradient(90deg, var(--blue-band) 0%, #7fb6fa 45%, #d9e9fd 80%, rgba(255,255,255,0) 100%);
    color: var(--paper);
    font-size: 13px;
    line-height: 21px;
    padding-left: 14px;
    white-space: nowrap;
  }
</style>
</head>
<body>
  <div class="signature">
    <div class="brand-name">Harbor Lantern</div>

    <ul class="contact-list">
      <li><span class="label">Tel.:</span> 555-014-2730</li>
      <li><span class="label">Fax:</span> 555-014-2730</li>
      <li><span class="label">Office:</span> 555-014-2736</li>
    </ul>

    <div class="web-links">
      <div>hello@harborlantern.net</div>
      <div>www.harborlantern.net</div>
    </div>

    <div class="social-icons">
      <svg width="12" height="12" viewBox="0 0 12 12" aria-label="Social profile"><circle cx="6" cy="6" r="5.5" fill="#7ee62a"/></svg>
      <svg width="12" height="12" viewBox="0 0 12 12" aria-label="Social profile"><circle cx="6" cy="6" r="5.5" fill="#7ee62a"/></svg>
      <svg width="17" height="12" viewBox="0 0 17 12" aria-label="Email">
        <rect x="0.5" y="0.5" width="16" height="11" fill="#7ee62a"/>
        <path d="M1 1 L8.5 7 L16 1" fill="none" stroke="#ffffff" stroke-width="1.2"/>
        <path d="M1 11 L6.5 5.5 M16 11 L10.5 5.5" fill="none" stroke="#ffffff" stroke-width="1"/>
      </svg>
    </div>

    <div class="address-band">418 West Quay Rd P.O. Box 7720 Bayford,&nbsp; USA 40217</div>
  </div>
</body>
</html>
```